Educational clinic needs a new webpage design

I have a relatively new website but I am unhappy with the design. I was hoping the look of it would more match my logo, brochures, business cards, and postcards. The content is good and it's already mobile ready. The designer used square space, which I would like to keep if possible. My website is www.harborlightstudyhouse.example

Target Market(s)

Parents of school age children

Industry/Entity Type

Education

Number of Pages Required

5+ page

Requirements
Must have
• Pictures must depict the diversity of our students. We service all ages, from preschool through college and our students come from varying races.
Should not have
• I try to avoid the word "tutoring" because what we do is so much more. I like the tag line of "results that go beyond traditional tutoring"

```html
<!DOCTYPE html>
<html lang="en">
<head>
<meta charset="utf-8">
<title>Harbor Light Study House</title>
<link rel="stylesheet" href="https://fonts.googleapis.com/css2?family=Oswald:wght@400;500&family=Roboto:wght@300;400;500&display=swap">
<style>
:root{
  --purple:#5c1f80;
  --purple-footer:#5e1c7b;
  --green:#9fbf3e;
  --green-dark:#8aab2e;
  --ink:#222;
  --text:#666;
  --muted:#888;
  --line:#ddd;
  --bg-grey:#f1f1f1;
  --bar:#1c1c1c;
  --white:#fff;
}
*{box-sizing:border-box;margin:0;padding:0}
html,body{width:1200px;height:2353px;overflow:hidden}
body{position:relative;background:var(--white);font-family:"Roboto",Arial,sans-serif;color:var(--text)}
.abs{position:absolute}
a{color:inherit;text-decoration:none}

/* header */
.brand{left:90px;top:26px;display:flex;align-items:center;gap:12px}
.brand-mark{width:50px;height:50px;border-radius:50%;background:var(--purple)}
.brand-name{font-size:25px;font-weight:500;color:var(--purple);line-height:1.1;width:250px}
.contact-top{left:522px;top:51px;font-size:16px;color:#333;display:flex;align-items:center;gap:10px}
.contact-top svg{fill:var(--purple)}
.contact-top .sep{margin:0 14px;color:#999}
.signup{left:1013px;top:42px;width:96px;height:38px;border:1.5px solid var(--purple);border-radius:4px;color:var(--purple);font-size:16px;display:flex;align-items:center;justify-content:center}

/* hero */
.hero{left:0;top:152px;width:1200px;height:620px;background:linear-gradient(90deg,#6a4a3a 0%,#a9896a 30%,#7b5446 55%,#3d3f4a 80%,#5b6b7d 100%)}
.nav{left:89px;top:111px;width:1025px;height:62px;background:var(--green);display:flex;z-index:2;box-shadow:0 2px 4px rgba(0,0,0,.2)}
.nav a{color:var(--white);font-size:16px;display:flex;align-items:center;justify-content:center;height:100%;text-transform:uppercase}
.nav a.active{background:var(--purple)}
.hero-caption{left:651px;top:552px;width:463px;height:134px;background:rgba(40,40,40,.7);color:var(--white);font-family:"Oswald",sans-serif;text-align:center;padding-top:20px}
.hero-caption .t1{font-size:48px;line-height:1;font-weight:400}
.hero-caption .t2{font-size:38px;line-height:1.15;font-weight:400}
.dots{left:1018px;top:742px;display:flex;gap:9px}
.dots span{width:11px;height:11px;border-radius:50%;background:var(--white)}
.dots span.on{background:var(--purple)}

/* welcome */
.welcome-title{left:0;top:827px;width:1200px;text-align:center;font-size:27px;color:var(--ink);font-weight:400}
.welcome-title em,.split-title em,.blog-title em{font-style:normal;color:var(--purple)}
.welcome-copy{left:96px;top:868px;width:1008px;text-align:center;font-size:13.5px;line-height:21px;color:var(--muted)}

/* feature cards */
.card{top:998px;width:243px;height:348px;background:var(--white);border:1px solid var(--line);box-shadow:0 12px 10px -8px rgba(0,0,0,.28);text-align:center}
.card-photo{height:166px}
.card h3{font-size:16px;font-weight:400;color:var(--ink);margin-top:36px;text-transform:uppercase}
.card p{font-size:12px;line-height:18px;color:var(--muted);padding:0 22px;margin-top:12px;height:72px;overflow:hidden}
.card .more{display:block;margin-top:22px;font-size:12.5px;color:var(--purple)}

/* why section */
.why{left:0;top:1387px;width:1200px;height:370px;background:var(--bg-grey)}
.video{left:89px;top:1443px;width:435px;height:264px;background:var(--white);border:1px solid #ccc;box-shadow:0 2px 6px rgba(0,0,0,.2);padding:9px}
.video-frame{position:relative;width:100%;height:100%;background:linear-gradient(160deg,#b9a678,#7f6b53 55%,#4d5a6a)}
.video-bar{position:absolute;left:0;bottom:0;width:100%;height:34px;background:#111;display:flex;align-items:center;padding:0 12px;gap:10px;color:var(--white);font-size:11px}
.split-title{left:562px;top:1457px;font-size:20px;color:var(--ink);font-weight:400;text-transform:uppercase}
.split-copy{left:560px;top:1494px;width:550px;font-size:12.5px;line-height:20px;color:#555}
.split-copy p+p{margin-top:18px}
.btn-more{left:557px;top:1661px;width:103px;height:38px;background:var(--green);color:var(--white);font-size:11px;display:flex;align-items:center;justify-content:center;border-radius:2px}

/* blog */
.blog-title{left:90px;top:1810px;font-size:21px;color:var(--ink);font-weight:400}
.blog-arrows{left:1090px;top:1810px;font-size:22px;color:#111}
.post{top:1859px;width:480px;display:flex;gap:18px}
.post-photo{width:161px;height:133px;flex:none}
.post h4{font-size:14px;font-weight:400;color:#333;margin-top:12px}
.post .date{font-size:12.5px;color:#555;margin-top:8px}
.post p{font-size:11.5px;line-height:18px;color:#555;margin-top:6px}
.post .more{font-size:12.5px;color:var(--purple);display:block;margin-top:6px}

/* footer */
.footer{left:0;top:2060px;width:1200px;height:225px;background:var(--purple-footer);color:var(--white)}
.fcol{top:2096px;font-size:11.5px;line-height:17px}
.fcol h5{font-size:15px;font-weight:400;text-transform:uppercase;margin-bottom:18px}
.fcol ul{list-style:none}
.fcol li{line-height:24px;font-size:11.5px}
.fcol li::before{content:"\25B8";font-size:9px;margin-right:8px}
.fcol .row{margin-bottom:14px}
.subscribe{display:flex;margin-top:14px}
.subscribe .field{width:140px;height:30px;background:#eee;color:#999;font-size:10px;display:flex;align-items:center;padding-left:12px}
.subscribe .go{width:62px;height:30px;background:#333;color:var(--white);font-size:12px;display:flex;align-items:center;justify-content:center}
.social{display:flex;gap:13px;margin-top:14px}
.social span{width:34px;height:34px;border:1.5px solid var(--white);border-radius:50%}
.bottom-bar{left:0;top:2285px;width:1200px;height:68px;background:var(--bar);color:var(--white);font-size:12px;text-align:center;padding-top:24px}
</style>
</head>
<body>

<header>
  <div class="abs brand"><span class="brand-mark"></span><span class="brand-name">Harbor Light Study House</span></div>
  <div class="abs contact-top">
    <svg width="16" height="12" viewBox="0 0 16 12"><rect width="16" height="12" rx="1"/><path d="M0 1 8 7 16 1" stroke="#fff" stroke-width="1.4" fill="none"/></svg>
    <span>info@HarborLightStudyHouse.example</span>
    <span class="sep">|</span>
    <svg width="14" height="14" viewBox="0 0 24 24"><path d="M6.6 10.8a15.1 15.1 0 0 0 6.6 6.6l2.2-2.2a1 1 0 0 1 1-.25 11.4 11.4 0 0 0 3.6.57 1 1 0 0 1 1 1V20a1 1 0 0 1-1 1A17 17 0 0 1 3 4a1 1 0 0 1 1-1h3.5a1 1 0 0 1 1 1c0 1.25.2 2.45.57 3.57a1 1 0 0 1-.25 1z"/></svg>
    <span>555-014-2290</span>
  </div>
  <a class="abs signup" href="#">SIGN UP</a>
</header>

<section class="abs hero" role="img" aria-label="Smiling student seated in a library with stacks of books behind her"></section>
<nav class="abs nav">
  <a class="active" href="#" style="width:120px">Home</a>
  <a href="#" style="width:152px">Services</a>
  <a href="#" style="width:152px">About Us</a>
  <a href="#" style="width:152px">Payments</a>
  <a href="#" style="width:122px">Blog</a>
  <a href="#" style="width:125px">News</a>
  <a href="#" style="width:182px">Contact</a>
</nav>
<div class="abs hero-caption"><div class="t1">TRADITIONAL TUTORING</div><div class="t2">We are an educational clinic</div></div>
<div class="abs dots"><span class="on"></span><span></span><span></span><span></span><span></span></div>

<h1 class="abs welcome-title">WELCOME TO <em>HARBOR LIGHT STUDY HOUSE</em></h1>
<p class="abs welcome-copy">Lorem Ipsum has been the industry's standard dummy text ever since the 1500s, when an unknown printer took a galley of type and scrambled it to make a type specimen book. It has survived not only five centuries, but also the leap into electronic typesetting, remaining essentially unchanged .It was popularised in the 1960s with the release of Typeset sheets containing Lorem Ipsum passages, and more recently with desktop publishing software like LayoutPro including versions of Lorem Ipsum</p>

<article class="abs card" style="left:89px">
  <div class="card-photo" role="img" aria-label="Young students smiling at a classroom table with crayons" style="background:linear-gradient(135deg,#e9b985,#d9874f 50%,#7aa6d6)"></div>
  <h3>Who We Are</h3>
  <p>This is the place for your 'elevator pitch.' If you only had a few seconds to pitch your products or services to someone, what would you say?</p>
  <a class="more" href="#">READ MORE &raquo;</a>
</article>
<article class="abs card" style="left:347px">
  <div class="card-photo" role="img" aria-label="Group of students reading books together at a desk" style="background:linear-gradient(135deg,#6b4a3c,#c9a07e 55%,#8c8fa8)"></div>
  <h3>Our Programs</h3>
  <p>We have many programs for an array of possible deficits. When parents bring their children to us, we want to have solutions for them.</p>
  <a class="more" href="#">READ MORE &raquo;</a>
</article>
<article class="abs card" style="left:607px">
  <div class="card-photo" role="img" aria-label="Children writing in notebooks outdoors on the grass" style="background:linear-gradient(135deg,#d7c3b0,#9bb86a 60%,#6e9a3c)"></div>
  <h3>How Can We Help?</h3>
  <p>At Harbor Light our primary goal is to diagnose the underlying cause for why a student may not be doing well in school.</p>
  <a class="more" href="#">READ MORE &raquo;</a>
</article>
<article class="abs card" style="left:866px">
  <div class="card-photo" role="img" aria-label="Young students drawing with pencils in class" style="background:linear-gradient(135deg,#c99a72,#e8cfb2 50%,#a8b7c2)"></div>
  <h3>Who Can We Help</h3>
  <p>We work with students of all ages who have challenges with listening, language and communication, reading, spelling, writing, comprehension, math, organiza-</p>
  <a class="more" href="#">READ MORE &raquo;</a>
</article>

<section class="abs why"></section>
<div class="abs video">
  <div class="video-frame" role="img" aria-label="Classroom of students raising hands as the teacher asks a question">
    <svg class="abs" style="left:185px;top:94px" width="46" height="46" viewBox="0 0 46 46"><circle cx="23" cy="23" r="22" fill="rgba(0,0,0,.55)" stroke="#fff" stroke-width="1.5"/><path d="M18 14 32 23 18 32z" fill="#fff"/></svg>
    <div class="video-bar">
      <svg width="14" height="14" viewBox="0 0 14 14"><circle cx="7" cy="7" r="6" fill="none" stroke="#fff" stroke-width="1.4"/><path d="M5.5 4.2 10 7 5.5 9.8z" fill="#fff"/></svg>
      <svg width="40" height="10" viewBox="0 0 40 10"><path d="M0 3h3l4-3v10l-4-3H0z" fill="#e23a5a"/><rect x="12" y="4" width="26" height="2" fill="#e23a5a"/></svg>
      <svg width="175" height="6" viewBox="0 0 175 6"><rect width="175" height="3" y="1.5" fill="#555"/><rect width="62" height="3" y="1.5" fill="#e23a5a"/></svg>
      <span>01:30 / 04:55</span>
      <svg width="34" height="12" viewBox="0 0 34 12"><rect x="1" y="2" width="12" height="8" fill="none" stroke="#fff"/><circle cx="28" cy="6" r="4" fill="none" stroke="#fff" stroke-width="2"/></svg>
    </div>
  </div>
</div>
<h2 class="abs split-title">Why Traditional Tutoring <em>Usually Does Not Help</em></h2>
<div class="abs split-copy">
  <p>When a student is &quot;tutored,&quot; the focus is on a content area, such as math or reading and that content is simply retaught. Although we do offer tutoring for students who need just a little help with content, most of what we do is very specialized. We want to find the root cause or the reason a perfectly bright student is struggling with academics.</p>
  <p>If the brain is not prepared for learning then reading, math, social studies, language arts, science can all be difficult If the brain is not prepared for learning then reading, math, social studies, language</p>
</div>
<a class="abs btn-more" href="#">READ MORE</a>

<h2 class="abs blog-title">LATEST <em>BLOG</em></h2>
<div class="abs blog-arrows">&lsaquo;&rsaquo;</div>
<article class="abs post" style="left:93px">
  <div class="post-photo" role="img" aria-label="Little girl smiling with a colouring book" style="background:linear-gradient(135deg,#f2d9d9,#e8b2a6 50%,#c5d7e6)"></div>
  <div>
    <h4>Nemo Enim Ipsam Volup</h4>
    <div class="date">09-07-2016</div>
    <p>Lorem Ipsum has been the industry's standard dummy text ever since the 1500s, when an unknown printer took a galley of type and scrambled it to make a type specimen book.</p>
    <a class="more" href="#">Read More &gt;&gt;</a>
  </div>
</article>
<article class="abs post" style="left:626px;top:1851px">
  <div class="post-photo" role="img" aria-label="Two young students smiling in front of a chalkboard" style="background:linear-gradient(135deg,#3e5a3a,#8a6a4e 50%,#d8b48e)"></div>
  <div>
    <h4>Nemo Enim Ipsam Volup</h4>
    <div class="date">09-07-2016</div>
    <p>Lorem Ipsum has been the industry's standard dummy text ever since the 1500s, when an unknown printer took a galley of type and scrambled it to make a type specimen book.</p>
    <a class="more" href="#">Read More &gt;&gt;</a>
  </div>
</article>

<footer>
  <div class="abs footer"></div>
  <div class="abs fcol" style="left:94px;top:2100px">
    <h5>Links</h5>
    <ul><li>Customer Support</li><li>Documentation</li><li>Resources</li><li>General FAQs</li><li>Shortcodes</li></ul>
  </div>
  <div class="abs fcol" style="left:274px;top:2098px;width:245px">
    <h5>Educational Clinic</h5>
    <p>Harbor Light Study House has been helping families with their educational needs for more than 10 years. We are more than passionate about students' success. At Harbor Light you'll find a welcoming environment, kind smiles and highly trained Learning Skills.</p>
  </div>
  <div class="abs fcol" style="left:599px;top:2100px;width:260px">
    <h5>Get In Touch</h5>
    <div class="row">Address : 418 Lantern Row, Brookfield, IL 60999</div>
    <div class="row">Phone :&nbsp; 555-014-2290</div>
    <div class="row">Email : info@HarborLightStudyHouse.example</div>
  </div>
  <div class="abs fcol" style="left:904px;top:2100px;width:210px">
    <h5>Newsletter</h5>
    <p>Your about us information would fit here nicely.</p>
    <div class="subscribe"><span class="field">Email address</span><span class="go">Submit</span></div>
    <div class="social"><span></span><span></span><span></span></div>
  </div>
  <div class="abs bottom-bar">Copyright &copy; 2016. All Rights Reserved</div>
</footer>

</body>
</html>
```